Brenmoor Estates Website and Logo Design

We need a new logo and website designed for 'Brenmoor Estates Ltd', which is a well established Guernsey property holding company founded in 1934.

The company does not currently have a website. The new website should be similar in style and layout to https://www.quillfenhouse.example/.

Target Market(s)

Industry, Media, Tenants

Industry/Entity Type

Property Management

Logo Text

BEL OR Brenmoor Estates Ltd OR BE

Coding

Coded - Design and coding required

Number of Pages Required

4 page

Font styles to use
Other font styles liked:
• Helvetica

Requirements
Must have
• The logo laying over the picture (like https://www.quillfenhouse.example/).
• Big pictures on homepage (like https://www.quillfenhouse.example/)

```html
<!DOCTYPE html>
<html lang="en">
<head>
<meta charset="utf-8">
<title>Brenmoor Estates Limited</title>
<link href="https://fonts.googleapis.com/css2?family=Cinzel:wght@400;700&family=Open+Sans:ital,wght@0,400;0,600;0,700;1,400&display=swap" rel="stylesheet">
<style>
:root{
  --blue:#2f5da3;
  --orange:#e8862a;
  --ink:#222;
  --muted:#666;
  --band:#eef1f6;
  --line:#d7d7d7;
  --white:#fff;
}
*{margin:0;padding:0;box-sizing:border-box}
html,body{width:1200px;height:2416px;overflow:hidden;background:var(--white)}
body{position:relative;font-family:"Open Sans",Helvetica,Arial,sans-serif;color:var(--ink)}
.abs{position:absolute}
.serif{font-family:"Cinzel",Georgia,serif}

/* hero */
.hero{left:0;top:0;width:1200px;height:524px;background:linear-gradient(180deg,#7f97bd 0%,#5f7fae 25%,#3f5f8e 55%,#2f4a6e 80%,#4a4a42 100%)}
.logo{left:72px;top:42px;display:flex;align-items:center;gap:14px;color:var(--white)}
.logo .mark{width:40px;height:40px;border:none;background:var(--white)}
.logo .name{font-family:"Cinzel",Georgia,serif;font-size:30px;font-weight:400;line-height:1.1;letter-spacing:1px}
.nav{left:419px;top:54px;display:flex;gap:24px;font-size:16px;color:var(--white);font-weight:600}
.nav .active{color:var(--orange)}
.nav svg{margin-top:2px}
.hero-title{left:0;width:1200px;top:175px;text-align:center;font-family:"Cinzel",Georgia,serif;font-size:62px;color:var(--white);letter-spacing:1px}
.hero-sub{left:0;width:1200px;top:250px;text-align:center;font-size:20px;color:var(--white)}
.btn-estimate{left:488px;top:293px;width:226px;height:39px;background:var(--orange);color:var(--white);font-size:15px;font-weight:700;display:flex;align-items:center;justify-content:center}
.dots{left:534px;top:475px;display:flex;gap:6px}
.dots span{width:30px;height:4px;background:var(--white)}
.dots span.on{background:var(--blue)}

/* welcome */
.section-title{left:0;width:1200px;text-align:center;font-family:"Cinzel",Georgia,serif;font-size:30px;color:var(--ink)}
.intro{left:180px;width:840px;top:610px;text-align:center;font-size:12.5px;line-height:24px;color:var(--muted)}
.card{top:688px;width:233px;height:251px;border:2px solid #e1e1e1;box-shadow:0 1px 3px rgba(0,0,0,.08);text-align:center}
.card .icon{position:absolute;left:61px;top:14px;width:110px;height:110px;border-radius:50%;background:var(--blue);box-shadow:0 0 0 3px #fff,0 0 0 5px var(--blue);display:flex;align-items:center;justify-content:center}
.card h3{position:absolute;top:137px;width:100%;font-family:"Cinzel",Georgia,serif;font-weight:400;font-size:16px}
.card p{position:absolute;top:164px;left:12px;right:12px;font-size:12px;line-height:21px;color:var(--muted)}
.card .more{position:absolute;top:218px;width:100%;font-size:12.5px;font-weight:700;color:var(--orange)}

/* why */
.why{left:0;top:999px;width:1200px;height:370px;background:var(--band)}
.why h2{left:98px;top:1040px;font-family:"Cinzel",Georgia,serif;font-weight:400;font-size:28px}
.why p{left:98px;width:500px;font-size:12.5px;line-height:24px;color:var(--muted)}
.btn-outline{border:1px solid #999;color:var(--orange);font-size:12.5px;font-weight:700;display:flex;align-items:center;justify-content:center}
.video{left:636px;top:1047px;width:464px;height:274px;border:4px solid var(--white);box-shadow:0 0 0 1px #ccc;background:linear-gradient(135deg,#e8e6e2 0%,#cfcac4 45%,#2a3550 85%)}
.play{left:834px;top:1148px;width:70px;height:70px;border-radius:50%;background:rgba(0,0,0,.55);border:3px solid var(--white)}

/* properties */
.prop-img{top:1481px;height:209px;box-shadow:0 1px 3px rgba(0,0,0,.2)}
.prop h3{font-weight:400;font-size:21px;color:var(--ink)}
.prop p{font-size:12.5px;line-height:24px;color:var(--muted)}
.prop .more{font-size:12.5px;font-weight:700;color:var(--orange)}

/* testimonial */
.quote-band{left:0;top:1894px;width:1200px;height:208px;background:var(--orange)}
.avatar{left:109px;top:1935px;width:126px;height:126px;border-radius:50%;border:4px solid var(--white);background:linear-gradient(160deg,#b9c3cf,#6f7c8a)}
.q-divider{left:269px;top:1935px;width:1px;height:126px;background:rgba(255,255,255,.7)}
.quote{left:303px;top:1938px;width:800px;font-style:italic;font-size:14px;line-height:27px;color:var(--white)}
.quote-name{left:303px;top:2036px;font-family:"Cinzel",Georgia,serif;font-size:18px;font-weight:700;color:var(--white)}

/* footer */
.footer-logo{left:72px;top:2205px;display:flex;align-items:center;gap:14px;color:var(--ink)}
.footer-logo .mark{width:40px;height:40px;background:var(--blue)}
.footer-logo .name{font-family:"Cinzel",Georgia,serif;font-size:30px;line-height:1.1;letter-spacing:1px}
.f-head{top:2150px;font-family:"Cinzel",Georgia,serif;font-size:18px;letter-spacing:1px}
.f-links{left:427px;top:2188px;list-style:none;font-size:12.5px;line-height:18px;color:#444}
.f-text{font-size:12.5px;line-height:22px;color:#444}
.f-input{left:596px;top:2241px;width:253px;height:35px;background:#efefef;border-bottom:1px solid #ccc;font-size:12px;color:#999;padding:9px 14px}
.f-sub{left:596px;top:2292px;width:92px;height:31px;font-size:11.5px}
.f-item{left:902px;display:flex;gap:12px;font-size:12.5px;line-height:22px;color:#444}
.f-item svg{flex:none;margin-top:4px}
.rule{left:98px;top:2354px;width:1004px;height:1px;background:var(--line)}
.copy{left:98px;top:2377px;font-size:12px;color:#555}
.social{top:2374px;width:26px;height:26px;border-radius:50%;border:1.5px solid var(--orange)}
</style>
</head>
<body>

<!-- hero -->
<div class="abs hero" role="img" aria-label="Photo of a calm harbour with small moored boats and rocky shoreline"></div>
<div class="abs logo"><span class="mark"></span><span class="name">BRENMOOR<br>ESTATES</span></div>
<nav class="abs nav">
  <span class="active">Home</span><span>About us</span><span>Services</span><span>Advisors</span><span>Investors</span><span>Careers</span><span>News</span><span>Contact Us</span>
  <svg width="16" height="16" viewBox="0 0 16 16"><circle cx="6.5" cy="6.5" r="5" fill="none" stroke="#fff" stroke-width="2"/><line x1="10" y1="10" x2="15" y2="15" stroke="#fff" stroke-width="2.4"/></svg>
</nav>
<h1 class="abs hero-title">BRENMOOR ESTATES LIMITED</h1>
<p class="abs hero-sub">Brenmoor Estates Limited (BEL) is a family-owned Guernsey property holding company</p>
<div class="abs btn-estimate">GET A FREE ESTIMATE</div>
<div class="abs dots"><span class="on"></span><span></span><span></span><span></span></div>

<!-- welcome -->
<h2 class="abs section-title" style="top:563px">Welcome to Brenmoor Estates Limited</h2>
<p class="abs intro">Brenmoor Estates Limited (BEL) is a family-owned Guernsey property holding company. It purchases properties that are considered to have potential for development either through refurbishment or by obtaining planning permission to change its classification from</p>

<div class="abs card" style="left:97px">
  <div class="icon"><svg width="52" height="46" viewBox="0 0 52 46"><path d="M3 3v40h46" fill="none" stroke="#fff" stroke-width="4"/><rect x="12" y="22" width="6" height="17" fill="#fff"/><rect x="22" y="12" width="6" height="27" fill="#fff"/><rect x="32" y="17" width="6" height="22" fill="#fff"/><rect x="42" y="8" width="5" height="31" fill="#fff"/></svg></div>
  <h3>Finance &amp; Accounting</h3>
  <p>There is no capital gains tax on the sale of property in the Island</p>
  <div class="more">READ MORE &gt;&gt;</div>
</div>
<div class="abs card" style="left:354px">
  <div class="icon"><svg width="56" height="50" viewBox="0 0 56 50"><path d="M28 3 L53 47 H3 Z" fill="#fff"/><rect x="25" y="17" width="6" height="17" fill="#2f5da3"/><rect x="25" y="37" width="6" height="6" fill="#2f5da3"/></svg></div>
  <h3>Risk &amp; Compilance</h3>
  <p>There is no capital gains tax on the sale of property in the Island</p>
  <div class="more">READ MORE &gt;&gt;</div>
</div>
<div class="abs card" style="left:612px">
  <div class="icon"><svg width="60" height="60" viewBox="0 0 60 60" fill="#fff"><path d="M30 2 L40 14 H33 V27 H46 V20 L58 30 L46 40 V33 H33 V46 H40 L30 58 L20 46 H27 V33 H14 V40 L2 30 L14 20 V27 H27 V14 H20 Z"/></svg></div>
  <h3>Approach</h3>
  <p>There is no capital gains tax on the sale of property in the Island</p>
  <div class="more">READ MORE &gt;&gt;</div>
</div>
<div class="abs card" style="left:868px">
  <div class="icon"><svg width="56" height="56" viewBox="0 0 56 56" fill="none" stroke="#fff" stroke-width="7"><path d="M10 24 A19 19 0 0 1 44 16"/><path d="M46 32 A19 19 0 0 1 12 40"/><path d="M48 4 V20 H32" fill="#fff" stroke="none"/><path d="M8 52 V36 H24" fill="#fff" stroke="none"/></svg></div>
  <h3>End - to - End</h3>
  <p>There is no capital gains tax on the sale of property in the Island</p>
  <div class="more">READ MORE &gt;&gt;</div>
</div>

<!-- why guernsey -->
<div class="abs why"></div>
<h2 class="abs" style="left:98px;top:1040px;font-family:'Cinzel',Georgia,serif;font-weight:400;font-size:28px">Why Guernsey?</h2>
<p class="abs" style="left:98px;top:1085px;width:500px;font-size:12.5px;line-height:24px;color:#666">The Bailiwick of Guernsey is a British Crown dependency in the English Channel. The benefit of establishing a company in Guernsey is the island's low tax jurisdiction since there are no capital taxes and no corporation taxes for many companies.</p>
<p class="abs" style="left:98px;top:1171px;width:500px;font-size:12.5px;line-height:24px;color:#666">Consequently since the 1980s the island's development as an ideal financial centre for the establishment of institutions and banks has thrived. There are currently more than 160 companies registered with the Island Financial Services Commission (28 banks, building societies, stock brokerage.</p>
<div class="abs btn-outline" style="left:98px;top:1284px;width:128px;height:35px">READ MORE &gt;&gt;</div>
<div class="abs video" role="img" aria-label="Video still of hands signing a document on a desk"></div>
<svg class="abs" style="left:834px;top:1148px" width="72" height="72" viewBox="0 0 72 72"><circle cx="36" cy="36" r="33" fill="rgba(0,0,0,.55)" stroke="#fff" stroke-width="3"/><path d="M28 22 L52 36 L28 50 Z" fill="#fff"/></svg>

<!-- properties -->
<h2 class="abs section-title" style="top:1418px">Our Properties</h2>

<div class="abs prop-img" style="left:97px;width:319px;background:linear-gradient(180deg,#3d6fc0 0%,#8aa8d8 30%,#c9c4b8 45%,#2a6b86 65%,#1d4f68 100%)" role="img" aria-label="Harbour town with boats on blue water"></div>
<div class="abs prop" style="left:97px;top:1708px;width:319px"><h3>Finibus Bonorum et Malorum</h3><p style="margin-top:10px">At vero eos et accusamus et iusto odio dignissimos duci mus qui blanditiis praesentium voluptatum deleniti atq ue corrupti quos dolores.</p><p class="more" style="margin-top:10px">READ MORE &gt;&gt;</p></div>

<div class="abs prop-img" style="left:440px;width:317px;background:linear-gradient(180deg,#9fb6d6 0%,#c5d0dd 30%,#5b6a5a 42%,#2e7e86 60%,#1f5c63 100%)" role="img" aria-label="Jetty with boats and an island on the horizon"></div>
<div class="abs prop" style="left:440px;top:1708px;width:317px"><h3>Finibus Bonorum et Malorum</h3><p style="margin-top:10px">At vero eos et accusamus et iusto odio dignissimos duci mus qui blanditiis praesentium voluptatum deleniti atq ue corrupti quos dolores.</p><p class="more" style="margin-top:10px">READ MORE &gt;&gt;</p></div>

<div class="abs prop-img" style="left:785px;width:317px;background:linear-gradient(180deg,#5a7fc4 0%,#9ab0d8 30%,#a8a49a 50%,#6e7580 75%,#3c4a58 100%)" role="img" aria-label="Marina full of yachts below a hillside town"></div>
<div class="abs prop" style="left:785px;top:1708px;width:317px"><h3>Finibus Bonorum et Malorum</h3><p style="margin-top:10px">At vero eos et accusamus et iusto odio dignissimos duci mus qui blanditiis praesentium voluptatum deleniti atq ue corrupti quos dolores.</p><p class="more" style="margin-top:10px">READ MORE &gt;&gt;</p></div>

<!-- testimonial -->
<div class="abs quote-band"></div>
<svg class="abs" style="left:36px;top:1982px" width="18" height="32" viewBox="0 0 18 32"><path d="M16 2 L3 16 L16 30" fill="none" stroke="#fff" stroke-width="3"/></svg>
<svg class="abs" style="left:1146px;top:1982px" width="18" height="32" viewBox="0 0 18 32"><path d="M2 2 L15 16 L2 30" fill="none" stroke="#fff" stroke-width="3"/></svg>
<div class="abs avatar" role="img" aria-label="Portrait photo of the client quoted"></div>
<div class="abs q-divider"></div>
<p class="abs quote">Nam libero tempore, cum soluta nobis est eligendi optio cumque nihil impedit quo minus id quod maxime placeat facere possimus, omnis voluptas assumenda est, omnis dolor repellendus. Temporibus autem quibusdam et aut officiis debitis aut rerum necessitatibus saepe eveniet ut et voluptates repudiandae sint et molestiae</p>
<p class="abs quote-name">- Marcel Durvanne</p>

<!-- footer -->
<div class="abs footer-logo"><span class="mark"></span><span class="name">BRENMOOR<br>ESTATES</span></div>

<h4 class="abs f-head" style="left:427px;font-weight:400">Information</h4>
<ul class="abs f-links"><li>Home</li><li>About us</li><li>Services</li><li>Advisors</li><li>Investors</li><li>Careers</li><li>News</li><li>Contact Us</li></ul>

<h4 class="abs f-head" style="left:596px;font-weight:400">Newsletter Subscription</h4>
<p class="abs f-text" style="left:596px;top:2189px;width:230px">Register your Email Address to get Information about us</p>
<div class="abs f-input">Email Address</div>
<div class="abs btn-outline f-sub">SUBSCRIBE</div>

<h4 class="abs f-head" style="left:902px;font-weight:400">Contact Us</h4>
<div class="abs f-item" style="top:2191px"><svg width="12" height="16" viewBox="0 0 12 16"><path d="M6 0 A6 6 0 0 1 12 6 C12 10 6 16 6 16 C6 16 0 10 0 6 A6 6 0 0 1 6 0 Z" fill="#e8862a"/><circle cx="6" cy="6" r="2.2" fill="#fff"/></svg><span>14 Harbour Row, Calder Quay<br>Sample Isle</span></div>
<div class="abs f-item" style="top:2254px"><svg width="14" height="14" viewBox="0 0 14 14"><path d="M3 0 L5.5 3.5 L4 5.5 C5 7.5 6.5 9 8.5 10 L10.5 8.5 L14 11 L12 14 C6 14 0 8 0 2 Z" fill="#e8862a"/></svg><span>+1-555-014-2290</span></div>
<div class="abs f-item" style="top:2296px"><svg width="15" height="12" viewBox="0 0 15 12"><rect width="15" height="12" fill="#e8862a"/><path d="M0 0 L7.5 6.5 L15 0" fill="none" stroke="#fff" stroke-width="1.4"/></svg><span>info@brenmoor-estates.example</span></div>

<div class="abs rule"></div>
<p class="abs copy">Copyrights © 2016, Brenmoor Estates Limited. All rights reserved.</p>
<span class="abs social" style="left:977px"></span>
<span class="abs social" style="left:1011px"></span>
<span class="abs social" style="left:1045px"></span>
<span class="abs social" style="left:1077px"></span>

</body>
</html>
```